Powepoint Templates From Logo

We need 3 Powerpoint templates for use in a variety of presentations we develop and customize. Primary uses of the powerpoint presentations are for printed "pitch books" describing our firm's capabilities and approach (a lot of words with some design elements that we have developed), printed presentations of the results of financial evaluations of our clients (lots of charts and graphs) and as the talking points for speeches.

The design needs to be professional and "solid" to establish that we are capable of selling your multi-million dollar business, but also be a little different to show that we are not just boring MBA's.

Our current website and other materials have been developed internally and leave a great deal to be desired. I have initiated this project to demonstrate how much our look can be improved and, if successful, I hope to do much bigger projects in the future.
Updates

This is my first project and I thaank you all for your participation. Since I am new to this, I don;t know if I am providing the help and feedback as I should. Please feel free to let me know how I can be a better customer.

Target Market(s)

professionals (lawyers, accountaants), business owners, business groups, technology people

Industry/Entity Type

Financial

Requirements
Must have
• our logo
a place where logo of client can be inserted if appropriate
templates for the following pages
title page
standard bullet narrative page
page for charts and graphs to mostly fill the page
Should not have a lot of dark solid color that has to be printed.

Nice to have
• something to perk up the color a little

```html
<!DOCTYPE html>
<html lang="en">
<head>
<meta charset="utf-8">
<title>Presentation Template Set</title>
<link rel="stylesheet" href="https://fonts.googleapis.com/css2?family=Arimo:wght@400;700&display=swap">
<style>
  :root{
    --navy:#1b2f5e;
    --ink:#1a1a1a;
    --charcoal:#231f20;
    --white:#ffffff;
    --stage:#e6e6e3;
    --bar-blue:#a9c1dc;
    --bar-green:#4caf50;
    --line-orange:#f39c12;
    --line-red:#c0392b;
    --grid:#c9c9c9;
  }
  *{box-sizing:border-box;margin:0;padding:0}
  html,body{width:1200px;height:900px;overflow:hidden}
  body{background:var(--stage);font-family:"Arimo",Arial,sans-serif;position:relative;color:var(--ink)}

  .slide{position:absolute;width:547px;height:409px;background:var(--white);overflow:hidden;box-shadow:0 2px 6px rgba(0,0,0,.18)}
  .slide--title{left:38px;top:38px}
  .slide--bullets{left:610px;top:38px}
  .slide--chart{left:38px;top:470px}
  .slide--closing{left:610px;top:470px;background:var(--navy)}

  /* Title slide */
  .brand{position:absolute;font-weight:700;color:var(--navy);letter-spacing:.5px;display:flex;align-items:center;gap:10px}
  .brand__square{width:22px;height:22px;border:3px solid var(--navy);border-radius:5px}
  .slide--title .brand{left:48px;top:160px;font-size:27px}
  .title-band{position:absolute;left:0;top:256px;width:100%;height:153px;background:var(--navy);padding:14px 0 0 66px;color:var(--white)}
  .title-band__heading{font-size:27px;font-weight:700;letter-spacing:.3px}
  .title-band__sub{font-size:12.5px;margin-top:6px;letter-spacing:.4px}

  /* Content slides */
  .slide-header{position:absolute;left:0;top:0;width:100%;height:60px;background:var(--navy);color:var(--white);font-size:23px;font-weight:700;padding:14px 0 0 34px}
  .slide-footer{position:absolute;left:0;bottom:0;width:100%;height:22px;background:var(--navy)}
  .slide-footer__tab{position:absolute;right:0;top:0;width:122px;height:22px;background:var(--charcoal)}
  .page-number{position:absolute;right:20px;bottom:4px;width:28px;height:28px;border-radius:50%;background:var(--white);border:2px solid var(--charcoal);font-size:17px;display:flex;align-items:center;justify-content:center;color:var(--ink)}

  .body-copy{font-size:12px;line-height:14.3px;text-align:justify;hyphens:auto}
  .slide--bullets .body-copy{position:absolute;left:43px;top:92px;width:210px}
  .bullet-list{position:absolute;left:256px;top:92px;width:208px;list-style:none}
  .bullet-list li{font-size:12px;line-height:14.3px;padding-left:22px;position:relative;margin-bottom:14px;text-align:justify}
  .bullet-list li::before{content:"";position:absolute;left:2px;top:2px;width:10px;height:10px;border:1.5px solid var(--navy);border-radius:2px}

  .chart{position:absolute;left:6px;top:100px;width:306px;height:210px}
  .chart__title{font-size:8px;font-weight:700}
  .chart__axis{font-size:5px;fill:#333}
  .slide--chart .body-copy{position:absolute;left:313px;top:108px;width:210px}

  .slide--closing .brand{left:0;right:0;top:188px;justify-content:center;color:var(--white);font-size:27px}
  .slide--closing .brand__square{border-color:var(--white)}
</style>
</head>
<body>

<section class="slide slide--title" aria-label="Title slide">
  <div class="brand"><span class="brand__square"></span>MERIDIAN KLVE</div>
  <div class="title-band">
    <h1 class="title-band__heading">LOREM IPSUM DOLOR SIT AMET</h1>
    <p class="title-band__sub">Lorem Ipsum Dolor sit Amet</p>
  </div>
</section>

<section class="slide slide--bullets" aria-label="Bullet narrative slide">
  <h2 class="slide-header">Lorem Ipsum Dolor Sit Amet</h2>
  <p class="body-copy">Lorem ipsum dolor sit amet, consectetur adipisicing elit, sed do eiusmod tempor incididunt ut labore et dolore magna aliqua. Ut enim ad minim veniam, quis nostrud exercitation ullamco laboris nisi ut aliquip ex ea commodo consequat. Duis aute irure dolor in reprehenderit in voluptate velit esse cillum dolore eu fugiat nulla pariatur. Excepteur sint occaecat cupidatat non proident, sunt in culpa qui officia deserunt mollit anim id est laborum</p>
  <ul class="bullet-list">
    <li>Lorem ipsum dolor sit amet, consectetur adipisicing elit,</li>
    <li>sed do eiusmod tempor incididunt ut labore et dolore magna aliqua.</li>
    <li>Ut enim ad minim veniam, quis nostrud exercitation ullamco laboris nisi ut aliquip ex ea commodo consequat.</li>
    <li>Duis aute irure dolor in reprehenderit in voluptate velit esse cillum dolore</li>
  </ul>
  <div class="slide-footer"><span class="slide-footer__tab"></span></div>
  <span class="page-number">1</span>
</section>

<section class="slide slide--chart" aria-label="Chart slide">
  <h2 class="slide-header">Lorem Ipsum Dolor Sit Amet</h2>
  <svg class="chart" viewBox="0 0 300 206" role="img" aria-label="Bar and line chart of bonus versus sales">
    <text class="chart__title" x="160" y="10" text-anchor="middle">Sales Employees - Bonus vs. SalesYTD</text>
    <g stroke="var(--grid)" stroke-width=".5">
      <line x1="40" y1="20" x2="292" y2="20"/><line x1="40" y1="46" x2="292" y2="46"/>
      <line x1="40" y1="72" x2="292" y2="72"/><line x1="40" y1="98" x2="292" y2="98"/>
      <line x1="40" y1="124" x2="292" y2="124"/><line x1="40" y1="150" x2="292" y2="150" stroke="#777"/>
    </g>
    <g class="chart__axis" text-anchor="end">
      <text x="37" y="22">100 %</text><text x="37" y="48">80 %</text><text x="37" y="74">60 %</text>
      <text x="37" y="100">40 %</text><text x="37" y="126">20 %</text><text x="37" y="152">0 %</text>
    </g>
    <g fill="var(--bar-blue)">
      <rect x="44" y="52.5" width="6" height="97.5"/><rect x="61.8" y="68.1" width="6" height="81.9"/>
      <rect x="79.6" y="74.6" width="6" height="75.4"/><rect x="97.4" y="77.2" width="6" height="72.8"/>
      <rect x="115.2" y="90.2" width="6" height="59.8"/><rect x="133" y="90.2" width="6" height="59.8"/>
      <rect x="150.8" y="95.4" width="6" height="54.6"/><rect x="168.6" y="98" width="6" height="52"/>
      <rect x="186.4" y="99.3" width="6" height="50.7"/><rect x="204.2" y="113.6" width="6" height="36.4"/>
      <rect x="222" y="121.4" width="6" height="28.6"/><rect x="239.8" y="135.7" width="6" height="14.3"/>
      <rect x="257.6" y="142.2" width="6" height="7.8"/>
    </g>
    <g fill="var(--bar-green)">
      <rect x="50" y="98" width="6" height="52"/><rect x="67.8" y="104.5" width="6" height="45.5"/>
      <rect x="85.6" y="56.4" width="6" height="93.6"/><rect x="103.4" y="82.4" width="6" height="67.6"/>
      <rect x="121.2" y="69.4" width="6" height="80.6"/><rect x="139" y="113.6" width="6" height="36.4"/>
      <rect x="156.8" y="90.2" width="6" height="59.8"/><rect x="174.6" y="92.8" width="6" height="57.2"/>
      <rect x="192.4" y="82.4" width="6" height="67.6"/><rect x="210.2" y="78.5" width="6" height="71.5"/>
      <rect x="228" y="52.5" width="6" height="97.5"/><rect x="245.8" y="78.5" width="6" height="71.5"/>
      <rect x="263.6" y="117.5" width="6" height="32.5"/><rect x="281.4" y="108.4" width="6" height="41.6"/>
    </g>
    <polyline fill="none" stroke="var(--line-orange)" stroke-width="1.6" points="49,134.4 66.8,121.4 84.6,104.5 102.4,91.5 120.2,78.5 138,69.4 155.8,59 173.6,48.6 191.4,39.5 209.2,33 227,29.1 244.8,25.2 262.6,22.6 280.4,21.3"/>
    <g fill="var(--line-orange)">
      <circle cx="49" cy="134.4" r="1.4"/><circle cx="66.8" cy="121.4" r="1.4"/><circle cx="84.6" cy="104.5" r="1.4"/>
      <circle cx="102.4" cy="91.5" r="1.4"/><circle cx="120.2" cy="78.5" r="1.4"/><circle cx="138" cy="69.4" r="1.4"/>
      <circle cx="155.8" cy="59" r="1.4"/><circle cx="173.6" cy="48.6" r="1.4"/><circle cx="191.4" cy="39.5" r="1.4"/>
      <circle cx="209.2" cy="33" r="1.4"/><circle cx="227" cy="29.1" r="1.4"/><circle cx="244.8" cy="25.2" r="1.4"/>
      <circle cx="262.6" cy="22.6" r="1.4"/><circle cx="280.4" cy="21.3" r="1.4"/>
    </g>
    <polyline fill="none" stroke="var(--line-red)" stroke-width="1.6" stroke-dasharray="4 2" points="49,143.5 66.8,137 84.6,124 102.4,121.4 120.2,111 138,100.6 155.8,95.4 173.6,85 191.4,74.6 209.2,59 227,46 244.8,33 262.6,26.5 280.4,22.6"/>
    <g class="chart__axis">
      <text x="110" y="72">61 %</text><text x="148" y="54">70 %</text><text x="170" y="42">86 %</text>
      <text x="188" y="34">88 %</text><text x="206" y="27">92 %</text><text x="226" y="24">97 %</text><text x="256" y="17">100 %</text>
    </g>
    <g class="chart__legend">
      <rect x="44" y="22" width="40" height="26" fill="#f7f0b0" stroke="#999" stroke-width=".4"/>
      <rect x="47" y="25" width="5" height="3" fill="var(--bar-blue)"/><text class="chart__axis" x="55" y="28">Bonus</text>
      <rect x="47" y="31" width="5" height="3" fill="var(--bar-green)"/><text class="chart__axis" x="55" y="34">Sales</text>
      <line x1="47" y1="38.5" x2="52" y2="38.5" stroke="var(--line-orange)"/><text class="chart__axis" x="55" y="40">Bonus Ratio</text>
      <line x1="47" y1="44.5" x2="52" y2="44.5" stroke="var(--line-red)" stroke-dasharray="2 1"/><text class="chart__axis" x="55" y="46">Sales YTD Ratio</text>
    </g>
    <g class="chart__axis" text-anchor="end">
      <text transform="translate(51 155) rotate(-90)">Rep 01</text><text transform="translate(68.8 155) rotate(-90)">Rep 02</text>
      <text transform="translate(86.6 155) rotate(-90)">Rep 03</text><text transform="translate(104.4 155) rotate(-90)">Rep 04</text>
      <text transform="translate(122.2 155) rotate(-90)">Rep 05</text><text transform="translate(140 155) rotate(-90)">Rep 06</text>
      <text transform="translate(157.8 155) rotate(-90)">Rep 07</text><text transform="translate(175.6 155) rotate(-90)">Rep 08</text>
      <text transform="translate(193.4 155) rotate(-90)">Rep 09</text><text transform="translate(211.2 155) rotate(-90)">Rep 10</text>
      <text transform="translate(229 155) rotate(-90)">Rep 11</text><text transform="translate(246.8 155) rotate(-90)">Rep 12</text>
      <text transform="translate(264.6 155) rotate(-90)">Rep 13</text><text transform="translate(282.4 155) rotate(-90)">Rep 14</text>
    </g>
  </svg>
  <p class="body-copy">Lorem ipsum dolor sit amet, consectetur adipisicing elit, sed do eiusmod tempor incididunt ut labore et dolore magna aliqua. Ut enim ad minim veniam, quis nostrud exercitation ullamco laboris nisi ut aliquip ex ea commodo consequat. Duis aute irure dolor in reprehenderit in voluptate velit esse cillum dolore eu fugiat nulla pariatur. Excepteur sint occaecat cupidatat non proident, sunt in culpa qui officia deserunt mollit anim id est laborum</p>
  <div class="slide-footer"><span class="slide-footer__tab"></span></div>
  <span class="page-number">2</span>
</section>

<section class="slide slide--closing" aria-label="Closing slide">
  <div class="brand"><span class="brand__square"></span>MERIDIAN KLVE</div>
</section>

</body>
</html>
```